I need the below text put into an illustration/high res image so I can print out and frame and give to my fiance. Can be simple but must look elegant. Idea is that the text can be written in the sand on the attached pics (let me know if you require more high res). Not precious on the dimensions but think no more than 90cm length or width. Can be smaller whatever you think works best. You can half long sentences if you think it will look better.
Update: some of you asked for a picture of us, not sure it works but have attached one
Marriage
Marriage isn’t for you.
You don’t marry to make yourself happy, you marry to make someone else happy.
More than that, your marriage isn’t for yourself, you’re marrying for a family.
Not just for the in-laws and all of that nonsense, but for your future children.
Who do you want to help you raise them?
Who do you want to influence them?
Marriage isn’t for you.
It’s not about you.
Marriage is about the person you married.

```html
<!DOCTYPE html>
<html lang="en">
<head>
<meta charset="utf-8">
<title>Marriage Isn't For You</title>
<link rel="stylesheet" href="https://fonts.googleapis.com/css2?family=Architects+Daughter&display=swap">
<style>
  :root {
    --sky-pale: #e4ebf1;
    --shore-light: #d9dde0;
    --sand-light: #cfc4b6;
    --sand-mid: #c3b6a5;
    --sand-dark: #b7a996;
    --etch: #675d53;
    --etch-light: rgba(255, 250, 240, 0.55);
    --glow: #f4f8fb;
    --portrait: #a59a8f;
  }
  * { margin: 0; padding: 0; box-sizing: border-box; }
  html, body { width: 1200px; height: 795px; overflow: hidden; background: var(--sand-mid); }
  .poster { position: relative; width: 1200px; height: 795px; overflow: hidden; }
  .beach-photo {
    position: absolute; inset: 0;
    background: linear-gradient(160deg, var(--sky-pale) 0%, var(--shore-light) 22%, var(--sand-light) 45%, var(--sand-mid) 75%, var(--sand-dark) 100%);
  }
  .couple-portrait {
    position: absolute; left: 30px; top: 2px; width: 320px; height: 285px;
    border-radius: 50%;
    background: radial-gradient(ellipse at 50% 50%, var(--portrait) 0%, #b7aea5 55%, var(--glow) 78%, rgba(244,248,251,0) 100%);
  }
  .sand-message {
    position: absolute; left: 360px; top: 0; width: 800px; height: 795px;
    font-family: "Architects Daughter", cursive;
    color: var(--etch);
    text-transform: uppercase;
    text-align: center;
    text-shadow: 0 1px 0 var(--etch-light), 0 -1px 0 rgba(70, 60, 50, 0.25);
    letter-spacing: 0.06em;
    list-style: none;
  }
  .sand-message .verse { position: absolute; left: 0; right: 0; white-space: nowrap; }
  .verse--1 { top: 178px; font-size: 15px; line-height: 17px; }
  .verse--2 { top: 216px; font-size: 19px; line-height: 20px; }
  .verse--3 { top: 280px; font-size: 20px; line-height: 23px; }
  .verse--4 { top: 352px; font-size: 22px; line-height: 27px; }
  .verse--5 { top: 438px; font-size: 24px; line-height: 26px; }
  .verse--6 { top: 501px; font-size: 25px; line-height: 27px; }
  .verse--7 { top: 571px; font-size: 26px; line-height: 28px; }
  .verse--8 { top: 647px; font-size: 29px; line-height: 31px; }
  .verse--9 { top: 736px; font-size: 30px; line-height: 32px; }
</style>
</head>
<body>
<main class="poster">
  <div class="beach-photo" role="img" aria-label="Beach photograph: sandy shore with gentle waves and a distant headland, a heart and a white rose in the sand"></div>

  <div class="couple-portrait" role="img" aria-label="Portrait photograph of the couple embracing, framed in a soft white oval"></div>

  <ul class="sand-message">
    <li class="verse verse--1">Marriage isn't for you.</li>
    <li class="verse verse--2">You don't marry to make yourself happy,<br>you marry to make someone else happy.</li>
    <li class="verse verse--3">More than that, your marriage isn't for yourself,<br>you're marrying for a family.</li>
    <li class="verse verse--4">Not just for the in-laws and all of that nonsense,<br>but for your future children.</li>
    <li class="verse verse--5">Who do you want to help you raise them?</li>
    <li class="verse verse--6">Who do you want to influence them?</li>
    <li class="verse verse--7">Marriage isn't for you.</li>
    <li class="verse verse--8">It's not about you</li>
    <li class="verse verse--9">Marriage is about the person you married.</li>
  </ul>
</main>
</body>
</html>
```